Bref créative
Brisk Mug Co
Stationary pack - card, compliment slip, headed paper.
Bright & Fun-filled
Tom Reeve
Managing Director
14 Fenwick Rd
Glenmorrow
Ardlanshire
Scotland
KA7 2QP
tbc
tom@briskmugco.com
www.briskmugco.com
This is our logo. We would obviously like something to tie inn with this.

```html
<!DOCTYPE html>
<html lang="en">
<head>
<meta charset="utf-8">
<title>Brisk Mug Co — Stationery Pack</title>
<link href="https://fonts.googleapis.com/css2?family=Nunito:wght@700;800;900&family=Roboto+Slab:wght@400;700&display=swap" rel="stylesheet">
<style>
  :root {
    --backdrop: #ebe7e1;
    --paper: #ffffff;
    --navy: #1c4a6c;
    --orange: #f59a1f;
    --sky: #8cc9ee;
    --blue-deep: #3f86c0;
    --blue-light: #86bfe8;
    --teal-ink: #1f8fc4;
    --yellow: #fff27a;
    --mist: #dde3e8;
    --wish: #8cc4ea;
  }
  * { box-sizing: border-box; margin: 0; padding: 0; }
  html, body { width: 1200px; height: 901px; overflow: hidden; }
  body {
    background: var(--backdrop);
    position: relative;
    font-family: "Roboto Slab", serif;
    font-weight: 700;
  }
  .sheet { position: absolute; background: var(--paper); box-shadow: 0 2px 6px rgba(0,0,0,.18); }

  .brand-name {
    font-family: "Nunito", sans-serif;
    font-weight: 900;
    letter-spacing: .5px;
    white-space: nowrap;
  }

  /* Headed paper */
  .letterhead { left: 12px; top: 20px; width: 563px; height: 710px; }
  .letterhead .logo-box {
    position: absolute; left: 20px; top: 14px; width: 129px; height: 85px;
    background: var(--navy); display: flex; align-items: center; justify-content: center;
  }
  .letterhead .logo-box .brand-name { color: #fff; font-size: 17px; }
  .letterhead .info-band {
    position: absolute; left: 166px; top: 14px; width: 387px; height: 85px;
    background: var(--orange); padding: 12px 10px;
    font-size: 9.5px; line-height: 22px; color: var(--yellow); white-space: nowrap;
  }

  /* Business card front (vertical) */
  .card-front {
    left: 604px; top: 15px; width: 278px; height: 484px;
    background: radial-gradient(ellipse at 40% 38%, var(--blue-light) 0%, var(--blue-deep) 75%);
    display: flex; align-items: center; justify-content: center;
  }
  .card-front .brand-name { color: #fff; font-size: 30px; margin-top: -30px; }

  /* Business card name side */
  .card-name {
    left: 901px; top: 12px; width: 224px; height: 232px;
    background: var(--orange); text-align: center;
  }
  .card-name .brand-name { display: block; margin-top: 38px; font-size: 22px; color: var(--navy); }
  .card-name .person { margin-top: 62px; font-family: "Nunito", sans-serif; font-weight: 800; font-size: 36px; color: var(--teal-ink); white-space: nowrap; }
  .card-name .role { font-family: "Nunito", sans-serif; font-weight: 800; font-size: 14px; color: #fff; margin-top: -2px; }

  /* Business card contact side */
  .card-contact {
    left: 906px; top: 275px; width: 219px; height: 219px;
    background: var(--sky); padding: 34px 14px;
    font-size: 10.5px; line-height: 15px; color: var(--navy); white-space: nowrap;
  }
  .card-contact .block + .block { margin-top: 22px; }

  /* Compliment slip */
  .comp-slip { left: 580px; top: 502px; width: 603px; height: 379px; }
  .comp-slip .greeting {
    position: absolute; left: 30px; top: 28px;
    font-family: "Nunito", sans-serif; font-weight: 800; font-size: 38px; color: var(--wish);
  }
  .comp-slip .faint-name {
    position: absolute; left: 0; right: 0; top: 150px; text-align: center;
    font-size: 34px; color: var(--mist);
  }
  .comp-slip .logo-box {
    position: absolute; left: 17px; top: 272px; width: 141px; height: 90px;
    background: var(--sky); display: flex; align-items: center; justify-content: center;
  }
  .comp-slip .logo-box .brand-name { color: var(--navy); font-size: 18px; }
  .comp-slip .info-band {
    position: absolute; left: 170px; top: 272px; width: 414px; height: 90px;
    background: var(--navy); color: #fff; font-size: 9.5px; line-height: 15px;
    display: flex; gap: 22px; padding: 14px 18px; white-space: nowrap;
  }
</style>
</head>
<body>

  <section class="sheet letterhead" aria-label="Headed paper">
    <div class="logo-box"><span class="brand-name">Brisk Mug Co</span></div>
    <div class="info-band">
      <p>Address: 14 Fenwick Rd,Glenmorrow,Ardlanshire,Scotland,KA7 2QP</p>
      <p>Web address: www.briskmugco.com</p>
      <p>Tel: 07700 900123</p>
    </div>
  </section>

  <section class="sheet card-front" aria-label="Business card front">
    <span class="brand-name">Brisk Mug Co</span>
  </section>

  <section class="sheet card-name" aria-label="Business card name side">
    <span class="brand-name">Brisk Mug Co</span>
    <p class="person">Tom Reeve</p>
    <p class="role">Managing Director</p>
  </section>

  <section class="sheet card-contact" aria-label="Business card contact side">
    <div class="block">
      <p>Address: 14 Fenwick Rd</p>
      <p>Glenmorrow</p>
      <p>Ardlanshire</p>
      <p>Scotland,KA7 2QP</p>
    </div>
    <div class="block">
      <p>Tel: 07700 900123</p>
      <p>Email: tom@briskmugco.com</p>
      <p>Web address: www.briskmugco.com</p>
    </div>
  </section>

  <section class="sheet comp-slip" aria-label="Compliment slip">
    <p class="greeting">Best Wishes.....</p>
    <p class="faint-name brand-name">Brisk Mug Co</p>
    <div class="logo-box"><span class="brand-name">Brisk Mug Co</span></div>
    <div class="info-band">
      <div>
        <p>Address: 14 Fenwick Rd</p>
        <p>Glenmorrow</p>
        <p>Ardlanshire</p>
        <p>Scotland,KA7 2QP</p>
      </div>
      <div>
        <p>Tel: 07700 900123</p>
        <p>Email: tom@briskmugco.com</p>
        <p>Web address: www.briskmugco.com</p>
      </div>
    </div>
  </section>

</body>
</html>
```